Create a new dynamic Video Production company website

A new website for a video production company. It needs to be focused on the videos with an easy to use and versatile video player. I want to be able to update (add/remove/edit) the videos myself and change some other regular information like price lists. Current website is www.reelvantor.ca
The new pages will be - Home - Corporate - Ministry - Wedding - Events - Contact

I was asked about Wordpress - I am not against WordPress so long as the designing company sets everything up properly. I have had bad experiences with Wordpress security (and spam) so as long as those issues are addressed, I can work with Wordpress.

• Video player that scales to different platforms - computers, tablets, cell phones etc.

```html
<!DOCTYPE html>
<html lang="en">
<head>
<meta charset="utf-8">
<title>Reelvantor Video Productions</title>
<link href="https://fonts.googleapis.com/css2?family=Open+Sans:wght@400;600;700&family=Roboto+Condensed:wght@400;700&display=swap" rel="stylesheet">
<style>
:root{
  --red:#c8101f;
  --red-dark:#9e0a14;
  --ink:#1e1e1e;
  --body:#555;
  --muted:#777;
  --line:#e3e3e3;
  --white:#fff;
  --dark:#1f1f1f;
  --footer:#ececec;
}
*{box-sizing:border-box;margin:0;padding:0}
html,body{width:1200px;height:3822px;overflow:hidden}
body{position:relative;background:var(--white);font-family:"Open Sans",Arial,sans-serif;color:var(--body)}
.abs{position:absolute}
.heading{font-family:"Roboto Condensed",Arial,sans-serif;font-weight:400;color:var(--ink);text-transform:uppercase;letter-spacing:.5px}
.center{left:0;width:1200px;text-align:center}

/* header */
.site-header{top:0;left:0;width:1200px;height:110px;background:var(--white)}
.brand{display:flex;align-items:center;gap:10px;font-family:"Roboto Condensed",Arial,sans-serif;font-weight:700;font-size:36px;color:var(--ink);letter-spacing:1px}
.brand-dot{width:30px;height:30px;border-radius:50%;background:var(--ink)}
.site-header .brand{position:absolute;left:84px;top:30px}
.main-nav a{position:absolute;top:38px;font-size:17px;color:var(--ink);text-decoration:none}
.main-nav a.active{color:var(--red)}
.main-nav a.active::after{content:"";position:absolute;left:0;right:0;bottom:-10px;height:3px;background:var(--red)}

/* hero */
.hero{top:110px;left:0;width:1200px;height:660px}
.hero-photo{position:absolute;inset:0;background:linear-gradient(110deg,#4a4f58 0%,#8b8f95 35%,#c9c3bb 60%,#e8e2d8 80%,#b9b2a7 100%);clip-path:polygon(0 0,100% 0,100% 508px,50% 648px,0 508px)}
.hero-title{position:absolute;left:240px;top:220px;font-family:"Roboto Condensed",Arial,sans-serif;font-weight:700;font-size:74px;color:var(--white);letter-spacing:1px;text-shadow:0 2px 6px rgba(0,0,0,.35)}
.hero-sub{position:absolute;left:300px;top:310px;font-family:"Roboto Condensed",Arial,sans-serif;font-size:34px;color:var(--white);text-shadow:0 2px 6px rgba(0,0,0,.35)}
.hero-arrow{position:absolute;top:278px;width:28px;height:28px;border-radius:50%;background:rgba(0,0,0,.45)}
.hero-edge{position:absolute;left:0;top:0}

/* welcome */
.welcome-title{left:89px;top:884px;font-size:34px}
.welcome-text{left:89px;top:936px;width:520px;font-size:12.5px;line-height:23px}
.btn-red{display:inline-block;background:var(--red);color:var(--white);border-radius:20px;font-size:13px;text-decoration:none}
.welcome-btn{left:86px;top:1104px;padding:8px 18px}
.player{left:642px;top:869px;width:471px;height:283px;background:linear-gradient(135deg,#3e4a5a,#7f8a96 45%,#c7c0b8 70%,#5a5f68);overflow:hidden}
.player-bar{position:absolute;left:0;right:0;bottom:0;height:26px;background:rgba(20,20,20,.85)}
.player-progress{position:absolute;left:10px;right:10px;bottom:30px;height:3px;background:rgba(255,255,255,.35)}
.player-progress span{display:block;width:8%;height:100%;background:var(--red)}
.play{position:absolute;left:50%;top:50%;transform:translate(-50%,-50%)}

/* services */
.services{top:1248px;left:0;width:1200px;height:426px;background:linear-gradient(135deg,#b40c1a 0%,#d3141f 35%,#a30a14 65%,#c8101f 100%)}
.services .heading{color:var(--white);font-size:34px;position:absolute;top:72px;left:0;width:1200px;text-align:center}
.service{position:absolute;top:171px;width:180px;margin-left:-90px;text-align:center;color:var(--white)}
.service-ring{width:108px;height:108px;margin:0 auto;border:3px solid var(--white);border-radius:50%;display:flex;align-items:center;justify-content:center}
.service-label{margin-top:22px;font-size:18px;text-transform:uppercase}

/* portfolio */
.portfolio-title{top:1786px;font-size:34px}
.work{position:absolute;width:311px}
.work-thumb{height:183px;background:linear-gradient(135deg,#4b5563,#9aa1a8 55%,#d7d2c8)}
.work-thumb.alt{background:linear-gradient(135deg,#2d2a44,#6b4c8a 50%,#c59a7a)}
.work-thumb.warm{background:linear-gradient(135deg,#f0e2c8,#caa98a 50%,#6d6a6a)}
.work-caption{text-align:center;font-size:17px;color:#333;margin-top:14px}
.outline-btn{left:497px;top:2388px;width:214px;height:40px;border:1.5px solid var(--red);border-radius:20px;color:var(--red);font-size:13px;text-transform:uppercase;display:flex;align-items:center;justify-content:center}

/* price list */
.pricing{top:2540px;left:0;width:1200px;height:428px;background:linear-gradient(180deg,#2a2a2a,#1a1a1a 60%,#2f2d26)}
.pricing .heading{position:absolute;top:82px;left:0;width:1200px;text-align:center;color:var(--white);font-size:34px}
.pricing-text{position:absolute;left:215px;top:152px;width:770px;text-align:center;color:var(--white);font-size:13.5px;line-height:22.5px}
.pricing .btn-red{position:absolute;top:296px;height:40px;line-height:40px;font-size:18px;text-align:center}

/* blog */
.blog-title{top:3072px;font-size:34px}
.post{position:absolute;top:3167px;width:311px;height:303px;background:var(--white);box-shadow:0 1px 6px rgba(0,0,0,.18);text-align:center}
.post-img{height:163px;background:linear-gradient(135deg,#5a6170,#a7adb4 55%,#e2ddd3)}
.post-img.bright{background:linear-gradient(135deg,#f4d6a6,#e79a6a 50%,#7c7f88)}
.post-img.deep{background:linear-gradient(135deg,#1f2430,#4b5668 55%,#9aa3b0)}
.post-date{display:inline-block;background:var(--red-dark);color:var(--white);font-size:12px;padding:4px 12px;margin-top:-13px;position:relative}
.post-title{font-size:15px;color:#333;text-transform:uppercase;margin-top:14px}
.post-text{font-size:11px;line-height:16px;color:var(--muted);margin:8px 22px 0}
.post-more{font-size:11px;color:#555;margin-top:6px}

/* footer */
.site-footer{top:3540px;left:0;width:1200px;height:282px}
.footer-bg{position:absolute;left:0;top:0}
.site-footer .brand{position:absolute;left:0;width:1200px;justify-content:center;top:70px;font-size:34px}
.contact-line{position:absolute;top:145px;left:0;width:1200px;display:flex;justify-content:center;align-items:center;gap:16px;font-size:17px;color:#333}
.contact-line svg{vertical-align:-3px;margin-right:6px}
.footer-links{position:absolute;left:91px;top:214px;font-size:12px;color:#333}
.socials{position:absolute;left:489px;top:206px;display:flex;gap:9px}
.socials span{width:29px;height:29px;border:1.5px solid #555;border-radius:50%}
.copyright{position:absolute;left:896px;top:214px;font-size:12px;color:#333}
</style>
</head>
<body>

<header class="site-header abs">
  <div class="brand"><span class="brand-dot"></span>REELVANTOR</div>
  <nav class="main-nav">
    <a class="active" href="#" style="left:459px">Home</a>
    <a href="#" style="left:558px">Corporate</a>
    <a href="#" style="left:690px">Ministry</a>
    <a href="#" style="left:805px">Wedding</a>
    <a href="#" style="left:925px">Events</a>
    <a href="#" style="left:1037px">Contacts</a>
  </nav>
</header>

<section class="hero abs">
  <div class="hero-photo" role="img" aria-label="Wedding couple in a chandelier hall being filmed by a camera operator"></div>
  <svg class="hero-edge" width="1200" height="660" viewBox="0 0 1200 660">
    <polyline points="0,520 600,660 1200,520" fill="none" stroke="#c8101f" stroke-width="6"/>
  </svg>
  <div class="hero-title">REELVANTOR</div>
  <div class="hero-sub">Video Productions</div>
  <span class="hero-arrow" style="left:70px"><svg width="28" height="28"><path d="M16 9l-5 5 5 5" fill="none" stroke="#fff" stroke-width="2"/></svg></span>
  <span class="hero-arrow" style="left:1100px"><svg width="28" height="28"><path d="M12 9l5 5-5 5" fill="none" stroke="#fff" stroke-width="2"/></svg></span>
</section>

<section class="welcome">
  <h1 class="heading welcome-title abs">Welcome to Reelvantor</h1>
  <p class="welcome-text abs">At Reelvantor Video Productions, we create unique and original video productions for Ministry, Corporate or Personal events that will teach, inspire, and relive special moments for years to come. Wedding and event videography, tribute videos, teaching and training video, promotional video productions, live events, and the list goes on. We examine every detail of our projects to ensure the highest quality product is provided for our customers.</p>
  <a class="btn-red welcome-btn abs" href="#">Read More »</a>
  <div class="player abs" role="img" aria-label="Video player showing a camera filming a wedding ceremony">
    <svg class="play" width="64" height="46" viewBox="0 0 64 46"><rect width="64" height="46" rx="10" fill="rgba(0,0,0,.75)"/><path d="M26 14l14 9-14 9z" fill="#fff"/></svg>
    <div class="player-progress"><span></span></div>
    <div class="player-bar">
      <svg width="471" height="26"><path d="M12 8l8 5-8 5z" fill="#ddd"/><path d="M34 10h4l5-4v14l-5-4h-4z" fill="#ddd"/><rect x="420" y="9" width="10" height="8" fill="none" stroke="#ddd"/><rect x="442" y="8" width="12" height="10" fill="none" stroke="#ddd"/></svg>
    </div>
  </div>
</section>

<section class="services abs" role="img" aria-label="Red faceted background">
  <h2 class="heading">Our Services</h2>
  <div class="service" style="left:206px">
    <div class="service-ring"><svg width="40" height="28" viewBox="0 0 40 28"><rect x="2" y="4" width="24" height="20" rx="3" fill="#fff"/><path d="M27 12l11-7v18l-11-7z" fill="#fff"/></svg></div>
    <div class="service-label">Corporate</div>
  </div>
  <div class="service" style="left:464px">
    <div class="service-ring"><svg width="40" height="38" viewBox="0 0 40 38"><path d="M20 2L2 11h36z" fill="#fff"/><rect x="6" y="14" width="4" height="16" fill="#fff"/><rect x="14" y="14" width="4" height="16" fill="#fff"/><rect x="22" y="14" width="4" height="16" fill="#fff"/><rect x="30" y="14" width="4" height="16" fill="#fff"/><rect x="2" y="32" width="36" height="4" fill="#fff"/></svg></div>
    <div class="service-label">Ministry</div>
  </div>
  <div class="service" style="left:724px">
    <div class="service-ring"><svg width="46" height="34" viewBox="0 0 46 34"><circle cx="16" cy="18" r="12" fill="none" stroke="#fff" stroke-width="4"/><circle cx="30" cy="18" r="12" fill="none" stroke="#fff" stroke-width="4"/></svg></div>
    <div class="service-label">Wedding</div>
  </div>
  <div class="service" style="left:981px">
    <div class="service-ring"><svg width="36" height="36" viewBox="0 0 36 36"><rect x="3" y="6" width="30" height="27" rx="2" fill="none" stroke="#fff" stroke-width="3"/><rect x="3" y="6" width="30" height="7" fill="#fff"/><rect x="9" y="2" width="3" height="7" fill="#fff"/><rect x="24" y="2" width="3" height="7" fill="#fff"/><g fill="#fff"><rect x="8" y="17" width="4" height="4"/><rect x="16" y="17" width="4" height="4"/><rect x="24" y="17" width="4" height="4"/><rect x="8" y="25" width="4" height="4"/><rect x="16" y="25" width="4" height="4"/><rect x="24" y="25" width="4" height="4"/></g></svg></div>
    <div class="service-label">Events</div>
  </div>
</section>

<section class="portfolio">
  <h2 class="heading portfolio-title abs center">Portfolio</h2>
  <div class="work" style="left:110px;top:1873px"><div class="work-thumb" role="img" aria-label="Camera operators filming outdoors"><svg class="play" style="position:relative;left:136px;top:72px;transform:none" width="40" height="40"><circle cx="20" cy="20" r="19" fill="rgba(0,0,0,.5)" stroke="#fff" stroke-width="2"/><path d="M16 12l12 8-12 8z" fill="#fff"/></svg></div><div class="work-caption">Ipsum quia dolor</div></div>
  <div class="work" style="left:448px;top:1873px"><div class="work-thumb" role="img" aria-label="Videographer filming a wedding"><svg style="position:relative;left:136px;top:72px" width="40" height="40"><circle cx="20" cy="20" r="19" fill="rgba(0,0,0,.5)" stroke="#fff" stroke-width="2"/><path d="M16 12l12 8-12 8z" fill="#fff"/></svg></div><div class="work-caption">Dolorem ipsum quia</div></div>
  <div class="work" style="left:785px;top:1873px"><div class="work-thumb warm" role="img" aria-label="Crew filming an interview"><svg style="position:relative;left:136px;top:72px" width="40" height="40"><circle cx="20" cy="20" r="19" fill="rgba(0,0,0,.5)" stroke="#fff" stroke-width="2"/><path d="M16 12l12 8-12 8z" fill="#fff"/></svg></div><div class="work-caption">Neque porro quisquam</div></div>
  <div class="work" style="left:110px;top:2122px"><div class="work-thumb" role="img" aria-label="Editor working at a video editing desk"><svg style="position:relative;left:136px;top:72px" width="40" height="40"><circle cx="20" cy="20" r="19" fill="rgba(0,0,0,.5)" stroke="#fff" stroke-width="2"/><path d="M16 12l12 8-12 8z" fill="#fff"/></svg></div><div class="work-caption">Ipsum quia dolor</div></div>
  <div class="work" style="left:448px;top:2122px"><div class="work-thumb alt" role="img" aria-label="Camera filming a concert stage"><svg style="position:relative;left:136px;top:72px" width="40" height="40"><circle cx="20" cy="20" r="19" fill="rgba(0,0,0,.5)" stroke="#fff" stroke-width="2"/><path d="M16 12l12 8-12 8z" fill="#fff"/></svg></div><div class="work-caption">Dolorem ipsum quia</div></div>
  <div class="work" style="left:785px;top:2122px"><div class="work-thumb warm" role="img" aria-label="Camera on a handheld stabilizer"><svg style="position:relative;left:136px;top:72px" width="40" height="40"><circle cx="20" cy="20" r="19" fill="rgba(0,0,0,.5)" stroke="#fff" stroke-width="2"/><path d="M16 12l12 8-12 8z" fill="#fff"/></svg></div><div class="work-caption">Neque porro quisquam</div></div>
  <a class="outline-btn abs" href="#">See more of our work</a>
</section>

<section class="pricing abs" role="img" aria-label="Darkened film set with lighting equipment">
  <h2 class="heading">Price List</h2>
  <p class="pricing-text">At Reelvantor Video Productions, we create unique and original video productions for Ministry, Corporate or Personal events that will teach, inspire, and relive special moments for years to come. Wedding and event videography, tribute videos, teaching and training video, promotional video productions, live events, and the list goes on. We examine every detail of our projects to ensure the highest quality product is provided for our customers. Allow us to bring your thoughts, ideas and dreams, into a custom video production.</p>
  <a class="btn-red" href="#" style="left:334px;width:247px">Videography Packages</a>
  <a class="btn-red" href="#" style="left:609px;width:257px">Photography Packages</a>
</section>

<section class="blog">
  <h2 class="heading blog-title abs center">Latest Blog</h2>
  <article class="post" style="left:110px"><div class="post-img" role="img" aria-label="Two videographers with cameras"></div><span class="post-date">14th May 2017</span><h3 class="post-title">Neque porro quisquam</h3><p class="post-text">It has survived not only five centuries, but also the leap into electronic typesetting, remaining</p><div class="post-more">Read More »</div></article>
  <article class="post" style="left:448px"><div class="post-img bright" role="img" aria-label="Camera filming against warm bokeh lights"></div><span class="post-date">14th May 2017</span><h3 class="post-title">Neque porro quisquam</h3><p class="post-text">It has survived not only five centuries, but also the leap into electronic typesetting, remaining</p><div class="post-more">Read More »</div></article>
  <article class="post" style="left:785px"><div class="post-img deep" role="img" aria-label="Close-up of a professional video camera"></div><span class="post-date">14th May 2017</span><h3 class="post-title">Neque porro quisquam</h3><p class="post-text">It has survived not only five centuries, but also the leap into electronic typesetting, remaining</p><div class="post-more">Read More »</div></article>
</section>

<footer class="site-footer abs">
  <svg class="footer-bg" width="1200" height="282" viewBox="0 0 1200 282">
    <defs><linearGradient id="fg" x1="0" y1="0" x2="0" y2="1"><stop offset="0" stop-color="#f6f6f6"/><stop offset="1" stop-color="#e2e2e2"/></linearGradient></defs>
    <polygon points="0,78 600,14 1200,78 1200,282 0,282" fill="url(#fg)"/>
    <polyline points="0,78 600,14 1200,78" fill="none" stroke="#c8101f" stroke-width="5"/>
  </svg>
  <div class="brand"><span class="brand-dot"></span>REELVANTOR</div>
  <div class="contact-line">
    <span><svg width="16" height="16" viewBox="0 0 16 16"><path d="M3 1l3 1 1 3-2 2c1 2 2 3 4 4l2-2 3 1 1 3-2 2C7 15 1 9 1 3z" fill="#c8101f"/></svg>555.014.2290</span>
    <span>|</span>
    <span><svg width="18" height="14" viewBox="0 0 18 14"><rect width="18" height="14" rx="1" fill="#c8101f"/><path d="M1 1l8 6 8-6" fill="none" stroke="#fff" stroke-width="1.5"/></svg>info@reelvantor.ca</span>
  </div>
  <div class="footer-links">About us &nbsp;| &nbsp;Service &nbsp;| &nbsp;FAQ &nbsp;| &nbsp;Contacts</div>
  <div class="socials"><span></span><span></span><span></span><span></span><span></span><span></span></div>
  <div class="copyright">Copyright © 2017. All Rights Reserved</div>
</footer>

</body>
</html>
```